Updated brief for New ecommerce site needs a stunning business card that links to web site.

Updated business card brief. Please refer to the new files uploaded today (the last two) which show the background colour/style that we will be using in our web template for on-line trading, the grey marble concrete look.

Please see if you can use the grey marble background in the business card design in a way so it relates to our web template. It also needs to be transferable to banner ad, chatterbay ad etc.
brivo hub is a NEW eCommerce website which is commencing selling via tradlo & sellnook, used & damaged mobile phones & accessories, evolving into a full eCommerce store.

We like strong clean lines, use of a circle, in essence this will become our logo as well. Colours strong orange/Black/White The orange stronger than in CraftPanel #5352704 & grey marble as per file attached #153082

We love the use of a circle!! As we are evolving & moving forward this is what the circle represents to us……. ongoing change.

Front side with a circle with brivo hub in a modern font in the middle, brivo is in a strong orange and group is in black or white. On the reverse side, use layout as per Lumerax design from pelk.example. for icon details (not the boarder at top/botto).

This design is to meet www.pelk.example luxe cards specifications
Thank you we look forward to last minute inspiration.
Updates

Target Market(s)

Suppliers & business networking

Industry/Entity Type

Business

Contact Information for Business Card

Sam Ruiz
Director
mob +61 4987 6543
Locked Bag WXYZ 5678 QRS
sam@brivohub.example.au
www.brivohub.example.au

Requirements
Must have
• Design to meet www.pelk.example luxe business card specifications
• Colours - orange needs to be bold and strong & /black/white
• Circle with brivo hub in the middle
Nice to have
• Grey marble background incorporated into design in someway so it links with our web page.

```html
<!DOCTYPE html>
<html lang="en">
<head>
<meta charset="utf-8">
<title>brivo hub business card</title>
<link rel="stylesheet" href="https://fonts.googleapis.com/css2?family=Federo&family=Montserrat:wght@500;700&display=swap">
<style>
  :root {
    --orange: #f2962f;
    --black: #262626;
    --white: #ffffff;
    --backdrop: #dcd8d3;
    --card-edge: rgba(0, 0, 0, 0.12);
  }
  html, body {
    margin: 0;
    padding: 0;
    width: 1200px;
    height: 800px;
    overflow: hidden;
    background: var(--backdrop);
  }
  .canvas {
    position: relative;
    width: 1200px;
    height: 800px;
  }
  .card {
    position: absolute;
    top: 250px;
    width: 525px;
    height: 300px;
    overflow: hidden;
    box-shadow: 0 10px 30px var(--card-edge);
  }
  .card--front {
    left: 50px;
    background: var(--orange);
  }
  .card--back {
    left: 625px;
    background: var(--black);
  }
  .emblem {
    position: absolute;
    border-radius: 50%;
    display: flex;
    flex-direction: column;
    justify-content: center;
  }
  .card--front .emblem {
    width: 250px;
    height: 250px;
    left: 137px;
    top: 25px;
    background: var(--black);
    align-items: center;
  }
  .brand-name {
    font-family: "Federo", sans-serif;
    font-size: 52px;
    line-height: 1;
    color: var(--orange);
    letter-spacing: 1px;
  }
  .card--back .emblem {
    width: 230px;
    height: 230px;
    left: 70px;
    top: 35px;
    background: var(--orange);
    align-items: flex-end;
    padding-right: 34px;
    box-sizing: border-box;
    text-align: right;
  }
  .contact-name {
    font-family: "Montserrat", sans-serif;
    font-weight: 700;
    font-size: 28px;
    color: var(--black);
    margin: 0;
    line-height: 1.05;
  }
  .contact-role {
    font-family: "Montserrat", sans-serif;
    font-weight: 700;
    font-size: 24px;
    color: var(--white);
    margin: 2px 0 8px;
    letter-spacing: 1px;
  }
  .contact-address {
    font-family: "Montserrat", sans-serif;
    font-weight: 500;
    font-size: 14px;
    color: var(--white);
    font-style: normal;
    line-height: 1.4;
  }
</style>
</head>
<body>
  <main class="canvas">
    <section class="card card--front" aria-label="Card front">
      <div class="emblem">
        <span class="brand-name">brivo hub</span>
      </div>
    </section>
    <section class="card card--back" aria-label="Card back">
      <div class="emblem">
        <h1 class="contact-name">Sam Ruiz</h1>
        <p class="contact-role">DIRECTOR</p>
        <address class="contact-address">Locked Bag<br>WXYZ 5678 QRS</address>
      </div>
    </section>
  </main>
</body>
</html>
```